Design for a Note buying company that attracts landlords and seller financed notes

I need a card designed. I want a simple clean front with my logo and contact info. On the back I want some big and bold words to get a message across.

Our Company buys Notes (mortgages) and we want to convey the sense of financial security. Our number one market that we pursue is tired landlords.

If you want to understand our business you can visit our website. www.deedpaperlane.com

Do not use any Clip Art in the design, it will not be accepted. I want a custom designed card not something I could throw together myself. Simple clean and drive the message home.

Target Market(s)

Landlords, seller financed note holders

Industry/Entity Type

Mortgage

Contact Information for Business Card

Simple clean and bold. I need to grab the attention of the customer. It should convey a professional touch.

Font styles to use
Sans Serif

Colors
ec2229
ffffff

Requirements
Must have
• Clean front with logo and contact information
Front colors should match logo

Back should be bold and grab attention. Back colors are open to ideas
Nice to have
• The Back May use the phrase "No more Tentants, No more Toilets" "More Time, More Cash"

I'm open to other ideas about grabbing a landlords attention

I'm open to a square card design
I like cards with round corners as well
Should not have
• any clip art! must be custom designs.

```html
<!DOCTYPE html>
<html lang="en">
<head>
<meta charset="utf-8">
<title>Keystone Note Buyers – Business Card</title>
<link rel="stylesheet" href="https://fonts.googleapis.com/css2?family=Lato:ital,wght@0,400;0,700;1,700&display=swap">
<style>
  :root {
    --brand-red: #ec2229;
    --paper: #ffffff;
    --ink: #111111;
    --text-grey: #4a4a4a;
    --canvas: #ffffff;
    --card-w: 677px;
    --card-h: 387px;
  }
  * { box-sizing: border-box; margin: 0; padding: 0; }
  html, body {
    width: 1200px; height: 1200px; overflow: hidden;
    background: var(--canvas);
    font-family: "Lato", sans-serif;
  }
  .card {
    position: absolute;
    left: 266px;
    width: var(--card-w);
    height: var(--card-h);
  }
  .card--front { top: 166px; background: var(--paper); outline: 1px solid #e6e6e6; }
  .card--back { top: 657px; background: var(--brand-red); color: var(--paper); }

  .brand {
    position: absolute;
    left: 80px; top: 176px;
    display: flex; align-items: center; gap: 10px;
  }
  .brand__mark { width: 22px; height: 22px; background: var(--brand-red); }
  .brand__name { font-weight: 700; font-size: 22px; color: var(--ink); letter-spacing: 0.5px; }

  .contact { position: absolute; left: 354px; top: 108px; color: var(--text-grey); }
  .contact__name { font-weight: 700; font-size: 31px; color: var(--brand-red); line-height: 1.1; }
  .contact__company { font-size: 20.5px; line-height: 1.2; margin-bottom: 12px; }
  .contact__address { font-size: 20.5px; line-height: 1.2; margin-bottom: 12px; }
  .contact__line { display: flex; align-items: center; gap: 8px; font-size: 20.5px; line-height: 29px; }
  .contact__icon { width: 23px; height: 23px; flex: none; }

  .slogan {
    position: absolute; left: 27px; top: 164px;
    font-weight: 700; font-style: italic; font-size: 21px; line-height: 30px;
  }
  .back-brand {
    position: absolute; left: 372px; top: 176px;
    font-weight: 700; font-size: 26px; letter-spacing: 0.5px;
  }
</style>
</head>
<body>
  <section class="card card--front" aria-label="Card front">
    <div class="brand">
      <span class="brand__mark"></span>
      <span class="brand__name">Keystone Note Buyers</span>
    </div>
    <div class="contact">
      <h1 class="contact__name">Dana Whitfield</h1>
      <p class="contact__company">Keystone Capital Group</p>
      <p class="contact__address">P.O.Box 218<br>Millbrook, Kansas 67190</p>
      <p class="contact__line">
        <svg class="contact__icon" viewBox="0 0 24 24" aria-hidden="true">
          <circle cx="12" cy="12" r="12" fill="#ec2229"/>
          <path d="M8.2 5.5l2 3.2-1.3 1.4c.8 1.8 2.2 3.2 4 4l1.4-1.3 3.2 2-.9 2.4c-5 .2-9.6-4.4-9.4-9.4z" fill="#fff"/>
        </svg>
        316-555-0142
      </p>
      <p class="contact__line">
        <svg class="contact__icon" viewBox="0 0 24 24" aria-hidden="true">
          <circle cx="12" cy="12" r="12" fill="#ec2229"/>
          <rect x="6" y="8" width="12" height="8.5" fill="none" stroke="#fff" stroke-width="1.3"/>
          <path d="M6 8l6 5 6-5M6 16.5l4.5-4M18 16.5l-4.5-4" fill="none" stroke="#fff" stroke-width="1.1"/>
        </svg>
        info@deedpaperlane.com
      </p>
    </div>
  </section>

  <section class="card card--back" aria-label="Card back">
    <p class="slogan">"No more Tentants, No more Toilets"<br>"More Time, More Cash"</p>
    <p class="back-brand">Keystone Note Buyers</p>
  </section>
</body>
</html>
```